Sell the dream! Property investment proposal document

We are looking for a proposal document which outlines our vision for property development. The purpose of the document is to raise investment from investors - sell the dream!
Brief summary:
Fennel Crest Developments, is an emerging New Zealand property investment company with a focus on providing unique property investment opportunities.
Our expertise and capabilities in architectural modular homes provide us with a remarkable advantage in tackling the development of properties that are typically considered challenging, remote, or uniquely positioned.
Our specialization in this niche sector of property development not only sets us apart from competitors, but also paves the way for lucrative investment opportunities in the New Zealand property market.
Feel free to use any images from www.fennelcrest.co.nz
Target Market(s)
investors for a unique property development opportunity
Industry/Entity Type
luxury property development in unique locations throughout New Zealand
Font styles to use
Colors
Designer to choose only greyscale colors for use in the design.
Look and feel

```html
<!DOCTYPE html>
<html lang="en">
<head>
<meta charset="utf-8">
<title>Fennel Crest Developments — Investment Proposal</title>
<link rel="stylesheet" href="https://fonts.googleapis.com/css2?family=Inter:wght@400;600;700&display=swap">
<style>
:root{
  --ink:#0d0d0d;
  --paper:#ffffff;
  --rule:#cfcfcf;
  --stage-top:#ffffff;
  --stage-low:#e6e6e6;
  --photo-dark:#2a2a2a;
  --photo-mid:#8a8a8a;
  --photo-light:#d6d6d6;
  --muted:#333333;
}
*{margin:0;padding:0;box-sizing:border-box}
html,body{width:1200px;height:2887px;overflow:hidden}
body{
  position:relative;
  font-family:"Inter",Arial,sans-serif;
  color:var(--ink);
  background:linear-gradient(var(--stage-top) 0,var(--stage-top) 2055px,#dadada 2055px,var(--stage-low) 2200px,#f0f0f0 2887px);
}
.spread{position:absolute;display:flex;width:930px;height:657px;box-shadow:0 4px 10px rgba(0,0,0,.25)}
.page{position:relative;width:465px;height:657px;background:var(--paper);overflow:hidden}
.page + .page{border-left:1px solid var(--rule)}
.photo{position:absolute}
.ph-dark{background:linear-gradient(160deg,#5e6f80 0%,#9aa3a6 30%,#3a3a36 60%,#6b6a55 100%)}
.ph-night{background:linear-gradient(180deg,#3d5066 0%,#5b6670 45%,#1f2522 100%)}
.ph-dusk{background:linear-gradient(180deg,#b8c4d2 0%,#d9b99a 45%,#4a3a2e 100%)}
.ph-green{background:linear-gradient(180deg,#e9ece8 0%,#9aa59a 45%,#2b2e2b 100%)}
.ph-mono{background:linear-gradient(180deg,#9c9c9c 0%,#5c5c5c 55%,#3a3a3a 100%)}
.ph-sketch{background:linear-gradient(180deg,#ffffff 0%,#f1f1f1 60%,#e6e6e6 100%)}
.ph-pool{background:linear-gradient(180deg,#9bb0c4 0%,#6b7a86 45%,#5f7f97 100%)}
.ph-interior{background:linear-gradient(180deg,#6a5a48 0%,#2c2926 55%,#4e4a45 100%)}
.ph-rock{background:linear-gradient(180deg,#d8d8d8 0%,#3e3e3e 35%,#4d5d35 75%,#7a9a3a 100%)}
.ph-cover{background:linear-gradient(180deg,#e4e4e4 0%,#cfcfcf 40%,#8a8a8a 62%,#3a3a3a 80%,#151515 100%)}

.cover-black{background:#000}
.wordmark{position:absolute;left:18px;top:10px;font-weight:600;font-size:112px;letter-spacing:-6px;line-height:1;color:var(--ink)}
.brand{position:absolute;display:flex;align-items:center;gap:6px;font-weight:600;white-space:nowrap}
.brand .sq{display:inline-block;background:currentColor}
.brand-cover{right:30px;bottom:26px;color:#fff;font-size:13px}
.brand-cover .sq{width:8px;height:8px}
.brand-center{left:0;right:0;top:312px;justify-content:center;color:#fff;font-size:22px;gap:10px}
.brand-center .sq{width:12px;height:12px}
.brand-head{top:34px;font-size:8px;color:var(--ink)}
.brand-head .sq{width:5px;height:5px}
.brand-head.left{left:45px}
.brand-head.right{right:45px}
.contacts{position:absolute;left:55px;right:55px;bottom:28px;display:flex;justify-content:space-between;color:#fff;font-size:7.5px;line-height:1.35}
.contacts b{font-weight:700}
.social{display:flex;align-items:center;gap:3px}
.social .dot{width:6px;height:6px;border-radius:50%;background:#fff;display:inline-block}

.title{position:absolute;font-weight:700;font-size:16px;line-height:1}
.title::after{content:"";display:block;width:68px;height:4px;background:var(--ink);margin-top:7px}
.title.right-align{text-align:right}
.title.right-align::after{margin-left:auto}
.copy{position:absolute;font-size:7.6px;line-height:1.3;text-align:justify;color:var(--ink)}
.copy p + p{margin-top:9px}
.footer{position:absolute;bottom:30px;font-size:6.5px;font-weight:700}
.footer.left{left:45px}
.footer.right{right:45px}

.why{position:absolute;left:36px;top:410px;display:flex;align-items:center;gap:8px}
.why .bar{width:3px;height:22px;background:var(--ink)}
.why .label{font-size:9px;line-height:1;color:var(--muted)}
.why .label b{font-weight:700;color:var(--ink)}
.reasons{position:absolute;left:34px;top:442px;width:262px;list-style:none}
.reasons li{display:flex;gap:8px;margin-bottom:8px}
.reasons .num{flex:0 0 12px;height:12px;border-radius:50%;background:var(--ink);color:#fff;font-size:6.5px;font-weight:700;display:flex;align-items:center;justify-content:center;margin-top:1px}
.reasons h4{font-size:7px;font-weight:700;line-height:1.2}
.reasons p{font-size:6.2px;line-height:1.3}

.mini{position:absolute;transform-origin:0 0;transform:scale(.74)}
</style>
</head>
<body>

<!-- Spread 1: covers -->
<section class="spread" style="left:121px;top:116px">
  <div class="page">
    <div class="photo ph-cover" style="inset:0" role="img" aria-label="Black and white photo of a glass cantilevered house on a misty hillside"></div>
    <div class="wordmark">Fennel</div>
    <div class="brand brand-cover"><span class="sq"></span>Fennel Crest</div>
  </div>
  <div class="page cover-black">
    <div class="brand brand-center"><span class="sq"></span>Fennel Crest</div>
    <div class="contacts">
      <div><b>E-mail:</b> sales@fennelcrest.co.nz<br><b>Phone:</b> 09 555 0142</div>
      <div style="text-align:center">Visit us by appointment<br><b>Waimauku, Auckland</b></div>
      <div><span class="social"><span class="dot"></span><b>fennel_crest</b></span><span class="social"><span class="dot"></span><b>FennelCrestNZ</b></span></div>
    </div>
  </div>
</section>

<!-- Spread 2: overview & origins -->
<section class="spread" style="left:121px;top:806px">
  <div class="page">
    <div class="brand brand-head left"><span class="sq"></span>Fennel Crest</div>
    <div class="photo ph-dark" style="left:0;top:84px;width:465px;height:211px" role="img" aria-label="Dark clad modular home with timber deck among coastal shrubs"></div>
    <h2 class="title" style="left:45px;top:320px">Business Overview</h2>
    <div class="copy" style="left:45px;top:364px;width:355px">
      <p>Fennel Crest Developments, is an emerging New Zealand property investment company with a focus on providing unique property investment opportunities.</p>
      <p>Our expertise and capabilities in architectural modular homes provide us with a remarkable advantage in tackling the development of properties that are typically considered challenging, remote, or uniquely positioned.</p>
      <p>As a company, with 48 employees boasting a wealth of experience in handling complex architectural projects, making us well-equipped to navigate the intricacies and demands of such ventures.</p>
      <p>This advantage allows us to not only execute projects efficiently but also to deliver exceptional results within condensed time frames.</p>
      <p>By capitalizing on our ability to develop difficult, remote, or one-of-a-kind properties swiftly and effectively, Fennel Crest Developments offers investors a rare chance to engage in projects that promise exceptional profitability in the New Zealand property market.</p>
      <p>Our specialization in this niche sector of property development not only sets us apart from competitors, but also paves the way for lucrative investment opportunities in the New Zealand property market.</p>
    </div>
    <div class="footer left">fennelcrest.co.nz</div>
  </div>
  <div class="page">
    <div class="brand brand-head right"><span class="sq"></span>Fennel Crest</div>
    <h2 class="title" style="left:45px;top:82px">Business Origins</h2>
    <div class="copy" style="left:45px;top:124px;width:375px">
      <p>Fennel Crest Developments was established with the goal of transforming the property investment market in New Zealand by introducing an innovative approach that centers on architectural modular designs and streamlined project timelines.</p>
      <p>Driven by our enthusiasm for architecture and real estate, we have expanded our successful business model to not only offer financial opportunities for investors but also to expand on our passion for high-end architectural design.</p>
    </div>
    <div class="photo ph-night" style="left:45px;top:228px;width:185px;height:103px" role="img" aria-label="Modular home lit at dusk beside a pool"></div>
    <div class="photo ph-dusk" style="left:45px;top:336px;width:185px;height:82px" role="img" aria-label="Timber deck of a modular home overlooking the sea at sunset"></div>
    <div class="photo ph-green" style="left:237px;top:228px;width:183px;height:190px" role="img" aria-label="Black modular home with slatted screen set in hills"></div>
    <div class="copy" style="left:45px;top:452px;width:375px">
      <p>With a wealth of experience accumulated over the past six years in the construction and the property market, we are pivoting to focus solely on our property development initiatives, presenting completed Fennel projects to the market, in exclusive locations.</p>
      <p>These projects will boast high-quality standards, meticulous attention to detail and landscaping, and creative design elements.</p>
      <p>By introducing completed Fennel properties into the market, we aim to reach a wider audience, catering to individuals who prefer ready-to-occupy homes, over engaging in the design and construction process. This approach also simplifies the financing process for prospective buyers, as established properties are often preferred by financial lenders.</p>
    </div>
    <div class="footer right">fennelcrest.co.nz</div>
  </div>
</section>

<!-- Spread 3: advantage & financials -->
<section class="spread" style="left:121px;top:1481px">
  <div class="page">
    <div class="brand brand-head left"><span class="sq"></span>Fennel Crest</div>
    <div class="photo ph-sketch" style="left:0;top:100px;width:465px;height:145px" role="img" aria-label="Line drawing of a long modular home on a slope"></div>
    <div class="photo ph-pool" style="left:0;top:245px;width:212px;height:133px" role="img" aria-label="Long glazed modular home with pool and loungers"></div>
    <div class="photo ph-interior" style="left:220px;top:245px;width:245px;height:133px" role="img" aria-label="Interior kitchen and dining space opening to a covered deck"></div>
    <h2 class="title" style="left:45px;top:412px">Competitive Advantage</h2>
    <div class="copy" style="left:45px;top:455px;width:336px">
      <p>Our competitive advantage lies in the uniqueness of our property investment opportunities. Unlike traditional real estate companies, we focus on offering properties that are not only profitable but also aesthetically pleasing and unique. By catering to the tastes of architecture lovers, we set ourselves apart from the competition and attract a niche market of customers who appreciate the artistry and design of our projects.</p>
      <p>Additionally, the streamlined and condensed timelines facilitated by our modular approach provide quicker returns on investment.</p>
    </div>
    <div class="footer left">fennelcrest.co.nz</div>
  </div>
  <div class="page">
    <div class="brand brand-head right"><span class="sq"></span>Fennel Crest</div>
    <h2 class="title right-align" style="right:45px;top:94px">Financial Summary</h2>
    <div class="photo ph-mono" style="left:0;top:120px;width:190px;height:195px" role="img" aria-label="Modular home module being transported on a truck"></div>
    <div class="copy" style="left:205px;top:134px;width:215px">
      <p>In terms of financial projections, with each development, we anticipate a profit of 10%-20% which will be project dependent.</p>
      <p>This growth is fueled by the increasing demand for unique property investments in New Zealand and our ability to deliver high-quality services to the market in a condensed time frame, with heavily controlled costs.</p>
      <p>With a solid business model and a dedicated team, we are confident in our ability to achieve success and establish Fennel Crest Investments as a trusted name in the industry.</p>
      <p>New Zealand's property market has been experiencing steady growth over the years, making it an attractive destination for property investors. With its beautiful landscapes and strong economy, New Zealand offers a diverse range of investment opportunities for both local and international investors. The demand for quality properties in prime locations continues to rise, creating a favorable environment for property investment companies like ours that can lean on our modular benefits of being able to reach unique and remote locations.</p>
    </div>
    <div class="why"><span class="bar"></span><span class="label">Why choose<br><b>Fennel?</b></span><span class="bar"></span></div>
    <ol class="reasons">
      <li><span class="num">1</span><div><h4>Architecturally Designed</h4><p>Functionality, comfort and a touch of luxury through contemporary residential design. <b>Fennel</b> boasts Aotearoa Guild of Architects registered practitioners in its team to ensure the highest standards of design and construction.</p></div></li>
      <li><span class="num">2</span><div><h4>Finishing &amp; Quality</h4><p><b>Fennel homes</b> are made with high-quality materials, fittings, surfaces and finishes as part of our standard offering. Preference is given to New Zealand products — when possible — and to brands with a proven track record of quality and longevity.</p></div></li>
      <li><span class="num">3</span><div><h4>Controlled Costs &amp; Timeframes</h4><p><b>Fennel's</b> processes ensure that clear communication about scheduling and costs is maintained at all times.</p></div></li>
      <li><span class="num">4</span><div><h4>Delivered and Connected Anywhere</h4><p>Due to our modular and prefabricated systems we can deliver and assemble <b>Fennel homes</b> in difficult-to-reach locations and locations with minimal trade supply.</p></div></li>
    </ol>
    <div class="photo ph-rock" style="left:345px;top:410px;width:120px;height:195px" role="img" aria-label="Cantilevered modular home above a rocky grassy slope"></div>
    <div class="footer right">fennelcrest.co.nz</div>
  </div>
</section>

<!-- Reduced cover -->
<div class="mini" style="left:64px;top:2248px">
  <section class="spread" style="position:relative;width:465px">
    <div class="page">
      <div class="photo ph-cover" style="inset:0" role="img" aria-label="Black and white photo of a glass cantilevered house on a misty hillside"></div>
      <div class="wordmark">Fennel</div>
      <div class="brand brand-cover"><span class="sq"></span>Fennel Crest</div>
    </div>
  </section>
</div>

<!-- Reduced overview spread -->
<div class="mini" style="left:443px;top:2250px">
  <section class="spread" style="position:relative">
    <div class="page">
      <div class="brand brand-head left"><span class="sq"></span>Fennel Crest</div>
      <div class="photo ph-dark" style="left:0;top:84px;width:465px;height:211px" role="img" aria-label="Dark clad modular home with timber deck among coastal shrubs"></div>
      <h2 class="title" style="left:45px;top:320px">Business Overview</h2>
      <div class="copy" style="left:45px;top:364px;width:355px">
        <p>Fennel Crest Developments, is an emerging New Zealand property investment company with a focus on providing unique property investment opportunities.</p>
        <p>Our expertise and capabilities in architectural modular homes provide us with a remarkable advantage in tackling the development of properties that are typically considered challenging, remote, or uniquely positioned.</p>
        <p>As a company, with 48 employees boasting a wealth of experience in handling complex architectural projects, making us well-equipped to navigate the intricacies and demands of such ventures.</p>
        <p>This advantage allows us to not only execute projects efficiently but also to deliver exceptional results within condensed time frames.</p>
        <p>By capitalizing on our ability to develop difficult, remote, or one-of-a-kind properties swiftly and effectively, Fennel Crest Developments offers investors a rare chance to engage in projects that promise exceptional profitability in the New Zealand property market.</p>
        <p>Our specialization in this niche sector of property development not only sets us apart from competitors, but also paves the way for lucrative investment opportunities in the New Zealand property market.</p>
      </div>
      <div class="footer left">fennelcrest.co.nz</div>
    </div>
    <div class="page">
      <div class="brand brand-head right"><span class="sq"></span>Fennel Crest</div>
      <h2 class="title" style="left:45px;top:82px">Business Origins</h2>
      <div class="copy" style="left:45px;top:124px;width:375px">
        <p>Fennel Crest Developments was established with the goal of transforming the property investment market in New Zealand by introducing an innovative approach that centers on architectural modular designs and streamlined project timelines.</p>
        <p>Driven by our enthusiasm for architecture and real estate, we have expanded our successful business model to not only offer financial opportunities for investors but also to expand on our passion for high-end architectural design.</p>
      </div>
      <div class="photo ph-night" style="left:45px;top:228px;width:185px;height:103px" role="img" aria-label="Modular home lit at dusk beside a pool"></div>
      <div class="photo ph-dusk" style="left:45px;top:336px;width:185px;height:82px" role="img" aria-label="Timber deck of a modular home overlooking the sea at sunset"></div>
      <div class="photo ph-green" style="left:237px;top:228px;width:183px;height:190px" role="img" aria-label="Black modular home with slatted screen set in hills"></div>
      <div class="copy" style="left:45px;top:452px;width:375px">
        <p>With a wealth of experience accumulated over the past six years in the construction and the property market, we are pivoting to focus solely on our property development initiatives, presenting completed Fennel projects to the market, in exclusive locations.</p>
        <p>These projects will boast high-quality standards, meticulous attention to detail and landscaping, and creative design elements.</p>
        <p>By introducing completed Fennel properties into the market, we aim to reach a wider audience, catering to individuals who prefer ready-to-occupy homes, over engaging in the design and construction process. This approach also simplifies the financing process for prospective buyers, as established properties are often preferred by financial lenders.</p>
      </div>
      <div class="footer right">fennelcrest.co.nz</div>
    </div>
  </section>
</div>

</body>
</html>
```